Meadow Lantern Equine Refuge - Sponsorship Flyer

We require an A4 trifold flyer. Our colours are orange, black and white.
At The Meadow Lantern Equine Refuge, we have a number of our animals available for Sponsorship. The majority are horses or ponies reflecting our focus however from time to time other animals in need find the peace of our Sanctuary.

Your sponsorship donation helps with the cost of care for horses requiring long-term rehabilitation including ongoing vet care etc as more often than not, the horse will have arrived in poor condition.

For those horses that are unsound or aged, (but with quality of life) and therefore not suited for adoption, are allowed to live out their days here at the Sanctuary.

As a DGR* charity all donations over $2 are tax deductible.

We have two different sponsorship types…Keepers of MLER and Allies of MLER

Target Market(s)

Horse Lovers

Industry/Entity Type

Rescue

Font styles to use
Serif

Colors
EE7325
F08F49
F5BC92
FAE3D3
FDF4ED

Requirements
Must have
• KEEPERS of MLER Store/SPONSORSHIP/KEEPERS of MLER Our Guardian sponsors choose to be with us for the long term. Their regular donation helps cover the monthly costs involved with caring for our residents. We like to think of these special folk as Guardian Angels. Their generosity allows us to keep so many safe from harm in this magical place. Guardian Sponsors receive a personalised e-certificate as well as a six-monthly update. We also invite our Guardians to contact us to organise a visit to the Sanctuary at a mutually convenient time. Here, you can meet the horse or pony that has captured your heart. Sponsorship costs vary from $15 – $25 per week depending on the animal and its needs.
Should not have
• External sourced photos

```html
<!DOCTYPE html>
<html lang="en">
<head>
<meta charset="utf-8">
<title>Meadow Lantern Equine Refuge – Sponsorship Flyer</title>
<link href="https://fonts.googleapis.com/css2?family=Montserrat:wght@400;700;800&display=swap" rel="stylesheet">
<style>
  :root {
    --orange: #EE7325;
    --orange-mid: #F08F49;
    --orange-soft: #F5BC92;
    --charcoal: #2f3033;
    --ink: #2b2b2d;
    --body: #555759;
    --white: #ffffff;
  }
  html, body { margin: 0; padding: 0; overflow: hidden; }
  body { width: 1200px; height: 927px; background: var(--white); }
  .flyer {
    position: relative; width: 1200px; height: 927px; overflow: hidden;
    font-family: "Montserrat", sans-serif; background: var(--white);
  }
  .panel { position: absolute; top: 0; height: 927px; }
  .panel--left { left: 0; width: 400px; }
  .panel--middle { left: 400px; width: 400px; background: var(--charcoal); }
  .panel--right { left: 800px; width: 400px; }

  .photo-horse-portrait {
    position: absolute; left: 0; top: 520px; width: 400px; height: 407px;
    background: linear-gradient(180deg, #ffffff 0%, #eeecea 25%, #d8cdc2 55%, #b89a80 80%, #8f7767 100%);
  }
  .decor { position: absolute; inset: 0; width: 1200px; height: 927px; }

  .heading {
    position: absolute; margin: 0; color: var(--ink);
    font-weight: 800; font-size: 38px; line-height: 35px; letter-spacing: 0.2px;
  }
  .heading--keepers { left: 54px; top: 62px; }
  .heading--allies { left: 835px; top: 172px; }
  .heading--join { left: 446px; top: 87px; color: var(--white); font-size: 40px; line-height: 40px; }
  .subheading {
    position: absolute; left: 446px; top: 126px; margin: 0;
    color: var(--white); font-weight: 400; font-size: 22px;
  }
  .copy {
    position: absolute; color: var(--body);
    font-size: 16px; line-height: 22.7px; font-weight: 400;
  }
  .copy p { margin: 0 0 22.7px; }
  .copy--keepers { left: 54px; top: 144px; width: 320px; }
  .copy--allies { left: 835px; top: 271px; width: 330px; }
  .copy--join { left: 446px; top: 171px; width: 340px; color: var(--white); }

  .brand {
    position: absolute; left: 1010px; top: 826px;
    display: flex; align-items: center; gap: 8px;
  }
  .brand__name {
    color: var(--white); font-weight: 700; font-size: 13px; line-height: 15px;
    text-align: right; width: 100px;
  }
  .brand__mark { width: 32px; height: 56px; background: var(--white); }
</style>
</head>
<body>
<div class="flyer">
  <section class="panel panel--left">
    <div class="photo-horse-portrait" role="img" aria-label="Photo of a palomino pony with a long pale mane standing behind a weathered log fence"></div>
  </section>
  <section class="panel panel--middle"></section>
  <section class="panel panel--right"></section>

  <svg class="decor" viewBox="0 0 1200 927" aria-hidden="false">
    <defs>
      <linearGradient id="corner-sweep" x1="0" y1="0" x2="1" y2="0">
        <stop offset="0" stop-color="#EE7325"/>
        <stop offset="1" stop-color="#E4872B"/>
      </linearGradient>
      <linearGradient id="herd-tones" x1="0" y1="0" x2="0" y2="1">
        <stop offset="0" stop-color="#a9a98a"/>
        <stop offset="0.35" stop-color="#7a5a3e"/>
        <stop offset="0.7" stop-color="#5a3f2e"/>
        <stop offset="1" stop-color="#8a8a4e"/>
      </linearGradient>
      <linearGradient id="band-fade" x1="0" y1="0" x2="1" y2="0">
        <stop offset="0" stop-color="#EE7325" stop-opacity="0"/>
        <stop offset="0.45" stop-color="#F08F49" stop-opacity="0.75"/>
        <stop offset="1" stop-color="#EE5A25"/>
      </linearGradient>
    </defs>
    <path d="M891 0 Q990 82 1200 100 L1200 0 Z" fill="url(#corner-sweep)"/>
    <path d="M465 927 Q760 560 1200 534 L1200 927 Z" fill="url(#herd-tones)" role="img" aria-label="Photo of a herd of brown, bay and grey horses running across a grassy paddock"/>
    <path d="M610 770 Q860 560 1200 534 L1200 544 Q880 570 610 770 Z" fill="url(#band-fade)"/>
  </svg>

  <h2 class="heading heading--keepers">KEEPERS<br>&nbsp;of MLER</h2>
  <div class="copy copy--keepers">
    <p>Our Guardian sponsors choose to be with us for the long term. Their regular donation helps cover the monthly costs of caring for our residents. We like to think of these special folk as Guardian Angels.</p>
    <p>Their generosity allows us to keep so many safe from harm in this magical place.</p>
    <p>Guardian Sponsors receive a person-alised e-certificate and a six-monthly update. We also invite our Guardians to organise a visit to meet the horse or pony that has captured their heart.</p>
    <p>Sponsorship ranges from $15–$25 per week, depending on the animal’s needs.</p>
  </div>

  <h2 class="heading heading--join">JOIN US</h2>
  <p class="subheading">in Making a Difference</p>
  <div class="copy copy--join">
    <p>As a registered DGR charity, all donations over $2 are tax deductible.</p>
    <p>Contact Us:<br>The Meadow Lantern Equine Refuge</p>
    <p>Phone:<br>Email:<br>Website:</p>
    <p>Follow us on social media:<br>[Ikon Facetome, Snapgrid]</p>
  </div>

  <h2 class="heading heading--allies">ALLIES<br>of MLER</h2>
  <div class="copy copy--allies">
    <p>Allies of MLER support the Sanctuary with a flexible, heartfelt donation. This sponsorship is ideal for those who want to contribute but may not be able to commit long-term.</p>
    <p>Allies receive a digital thank-you note and occasional updates about our work and residents.</p>
  </div>

  <div class="brand">
    <span class="brand__name">Meadow Lantern Equine Refuge</span>
    <span class="brand__mark"></span>
  </div>
</div>
</body>
</html>
```